Design a refer a friend Flyer (French & English)
Flyer Title:
Main Title: "Refer a Friend & Receive a Free Electric Toothbrush!"
Bold and clear, centered at the top.
Use a clean and modern font.
Color: White text on a vivid green background for maximum contrast and readability.
Visual Focus:
Toothbrush Image: Place a high-quality image of the Denta-K Flex 300 Electric Toothbrush in the center of the flyer.
Include a small price tag with “Value of $50” near the toothbrush to highlight the reward.
Simple Message:
Text: "Refer a friend to Centre Dentaire Val-Morin. When they book and attend their appointment, you get a free electric toothbrush, and they receive a special gift!"
Straightforward and easy to understand.
Placed below the image of the toothbrush.
Referral Process:
3 Easy Steps:
Refer a Friend
They Book and Come to Their Appointment
Receive Your Free Electric Toothbrush
Use simple, minimal icons to visually represent each step.
Keep the steps aligned horizontally or vertically for clarity.
Call to Action:
Text: "Start Referring Today!"
Place it in a button-like design in the vivid green color with bold, white text to make it stand out.
Contact Information:
Details:
Logo of Centre Dentaire Val-Morin.
Address: "48 Lavigne Ouest, Suite 210".
Phone Number and Website: Positioned at the bottom for easy reference.
Color Scheme:
Use a vivid green background for the entire flyer, with white accents for text and icons to maintain a fresh, clean look.
Minimal clutter, focusing on clarity and the key elements: the toothbrush, the call to action, and contact information.
Clinic : www.cdvalmorin-example.com
Attached is the brandbook, logo and inspo I made with AI.
French text will be provided.
Thank you,
Tariq

```html
<!DOCTYPE html>
<html lang="en">
<head>
<meta charset="utf-8">
<title>Refer a Friend – Clinique Dentaire Val-Morin</title>
<link rel="stylesheet" href="https://fonts.googleapis.com/css2?family=Poppins:ital,wght@0,600;0,700;0,800;0,900;1,800;1,900&family=Roboto:wght@500;700&display=swap">
<style>
  :root {
    --green-top: #67a955;
    --green-low: #8cbb46;
    --green-deep: #5a8f45;
    --lime: #a9c93a;
    --yellow: #ffe816;
    --red: #c9201f;
    --ink: #333333;
    --white: #ffffff;
  }
  html, body {
    margin: 0;
    padding: 0;
    width: 927px;
    height: 1200px;
    overflow: hidden;
  }
  .flyer {
    position: relative;
    width: 927px;
    height: 1200px;
    overflow: hidden;
    background: linear-gradient(180deg, var(--green-top) 0%, var(--green-top) 45%, var(--green-low) 100%);
    font-family: "Poppins", sans-serif;
    color: var(--white);
  }
  .brand {
    position: absolute;
    left: 289px;
    top: 28px;
    font-family: "Roboto", sans-serif;
  }
  .brand-name {
    font-size: 31px;
    font-weight: 700;
    line-height: 1;
    letter-spacing: -0.3px;
  }
  .brand-place {
    font-size: 13px;
    font-weight: 700;
    margin-top: 6px;
  }
  .brand-dot {
    position: absolute;
    left: 590px;
    top: 36px;
    width: 30px;
    height: 30px;
    border-radius: 50%;
    background: var(--white);
  }
  .headline {
    position: absolute;
    left: 0;
    top: 118px;
    width: 927px;
    margin: 0;
    text-align: center;
    font-weight: 900;
    font-size: 88px;
    line-height: 90px;
    letter-spacing: -1.5px;
    text-transform: uppercase;
    white-space: nowrap;
  }
  .product-visual {
    position: absolute;
    left: 444px;
    top: 469px;
    width: 75px;
    height: 630px;
    border-radius: 34px 34px 18px 18px;
    background: linear-gradient(90deg, #111 0%, #2b2b2b 45%, #0d0d0d 100%);
  }
  .intro {
    position: absolute;
    left: 89px;
    top: 512px;
    margin: 0;
    color: var(--yellow);
    font-style: italic;
    font-weight: 900;
    font-size: 31px;
    line-height: 45px;
    letter-spacing: -1px;
    text-transform: uppercase;
  }
  .message {
    position: absolute;
    left: 89px;
    top: 663px;
    margin: 0;
    font-style: italic;
    font-weight: 800;
    font-size: 24px;
    line-height: 34px;
    letter-spacing: -0.5px;
  }
  .steps-title {
    position: absolute;
    left: 578px;
    top: 510px;
    margin: 0;
    font-weight: 800;
    font-size: 72px;
    line-height: 66px;
    letter-spacing: -1px;
  }
  .steps {
    position: absolute;
    left: 579px;
    top: 658px;
    margin: 0;
    padding: 0;
    list-style: none;
  }
  .step {
    position: absolute;
    left: 0;
    width: 320px;
    height: 78px;
    display: flex;
    align-items: center;
  }
  .step:nth-child(1) { top: 0; }
  .step:nth-child(2) { top: 96px; }
  .step:nth-child(3) { top: 195px; }
  .step-icon {
    width: 78px;
    height: 78px;
    flex: none;
  }
  .step-text {
    margin-left: 29px;
    font-weight: 800;
    font-size: 19px;
    line-height: 22px;
    text-transform: uppercase;
    letter-spacing: -0.3px;
  }
  .ground {
    position: absolute;
    left: 0;
    top: 975px;
    width: 927px;
    height: 225px;
  }
  .cta {
    position: absolute;
    left: 230px;
    top: 892px;
    width: 226px;
    height: 226px;
    border-radius: 50%;
    background: linear-gradient(135deg, var(--lime) 0%, var(--green-top) 50%, var(--green-top) 100%);
    display: flex;
    align-items: center;
    justify-content: center;
  }
  .cta-inner {
    width: 182px;
    height: 182px;
    border-radius: 50%;
    background: linear-gradient(160deg, var(--green-deep) 0%, var(--green-top) 55%, var(--lime) 100%);
    display: flex;
    align-items: center;
    justify-content: center;
    text-align: center;
    font-style: italic;
    font-weight: 900;
    font-size: 32px;
    line-height: 33px;
    letter-spacing: -0.5px;
  }
  .price-tag {
    position: absolute;
    left: 490px;
    top: 900px;
    width: 220px;
    height: 190px;
  }
  .footer {
    position: absolute;
    left: 0;
    top: 1165px;
    width: 927px;
    text-align: center;
    font-weight: 700;
    font-size: 17px;
    white-space: nowrap;
  }
  .footer .sep {
    color: var(--yellow);
    margin: 0 9px;
  }
</style>
</head>
<body>
<main class="flyer">
  <div class="brand">
    <div class="brand-name">Clinique Dentaire</div>
    <div class="brand-place">Val-Morin</div>
  </div>
  <span class="brand-dot"></span>

  <h1 class="headline">Refer a Friend<br>&amp; Receive<br>a Free Electric<br>Toothbrush!</h1>

  <svg class="ground" viewBox="0 0 927 225" preserveAspectRatio="none" aria-hidden="true">
    <path d="M0 52 Q 463 -10 927 30 L927 225 L0 225 Z" fill="var(--ink)"/>
  </svg>

  <p class="intro">Refer a friend to<br>Centre Dentaire<br>Val-Morin.</p>

  <p class="message">When they book and<br>attend their<br>appointment,<br>you get a free electric<br>toothbrush, and they<br>receive a special gift!</p>

  <div class="product-visual" role="img" aria-label="Photo of the black Denta-K Flex 300 electric toothbrush standing upright"></div>

  <h2 class="steps-title">3 Easy<br>Steps:</h2>

  <ol class="steps">
    <li class="step">
      <svg class="step-icon" viewBox="0 0 78 78" aria-hidden="true">
        <circle cx="39" cy="39" r="37" fill="none" stroke="var(--yellow)" stroke-width="2"/>
        <g fill="var(--yellow)">
          <circle cx="30" cy="22" r="4"/><circle cx="39" cy="20" r="4"/><circle cx="48" cy="22" r="4"/>
          <rect x="25" y="27" width="10" height="8" rx="3"/><rect x="34" y="25" width="10" height="10" rx="3"/><rect x="43" y="27" width="10" height="8" rx="3"/>
          <path d="M18 44 L30 40 Q44 40 56 44 L56 48 Q44 46 34 47 L46 50 Q58 48 62 44 L64 48 Q56 58 38 58 L18 54 Z"/>
        </g>
      </svg>
      <span class="step-text">Refer a Friend</span>
    </li>
    <li class="step">
      <svg class="step-icon" viewBox="0 0 78 78" aria-hidden="true">
        <circle cx="39" cy="39" r="37" fill="none" stroke="var(--yellow)" stroke-width="2"/>
        <g fill="var(--yellow)">
          <circle cx="26" cy="20" r="5"/><circle cx="52" cy="20" r="5"/>
          <rect x="20" y="27" width="12" height="22" rx="3"/><rect x="46" y="27" width="12" height="22" rx="3"/>
          <rect x="22" y="49" width="4" height="16"/><rect x="27" y="49" width="4" height="16"/>
          <rect x="47" y="49" width="4" height="16"/><rect x="52" y="49" width="4" height="16"/>
          <rect x="31" y="34" width="16" height="4" rx="2"/>
          <rect x="54" y="44" width="12" height="9" rx="1"/>
        </g>
      </svg>
      <span class="step-text">They book and<br>come to their<br>appointment</span>
    </li>
    <li class="step">
      <svg class="step-icon" viewBox="0 0 78 78" aria-hidden="true">
        <circle cx="39" cy="39" r="37" fill="none" stroke="var(--yellow)" stroke-width="2"/>
        <g fill="var(--yellow)">
          <path d="M16 60 L44 30 L50 36 L22 66 Q16 68 16 60 Z"/>
          <rect x="46" y="24" width="6" height="10" transform="rotate(45 49 29)"/>
          <circle cx="56" cy="20" r="8"/>
        </g>
        <circle cx="28" cy="54" r="2" fill="var(--green-low)"/>
      </svg>
      <span class="step-text">Receive your<br>free electric<br>toothbrush</span>
    </li>
  </ol>

  <div class="cta">
    <div class="cta-inner">Start<br>Referring<br>Today!</div>
  </div>

  <svg class="price-tag" viewBox="0 0 220 190" aria-label="Price tag: value of $50">
    <path d="M34 82 C 0 60 10 0 52 10" fill="none" stroke="#111" stroke-width="3"/>
    <path d="M32 70 L76 48 L206 84 L188 178 L54 152 L22 98 Z" fill="var(--yellow)" transform="rotate(2 110 110)"/>
    <circle cx="48" cy="88" r="7" fill="var(--green-low)" stroke="var(--white)" stroke-width="3"/>
    <text x="78" y="100" fill="var(--red)" font-family="Poppins, sans-serif" font-weight="800" font-size="13">VALUE OF</text>
    <text x="82" y="146" fill="var(--red)" font-family="Poppins, sans-serif" font-weight="900" font-size="48">$50</text>
  </svg>

  <footer class="footer">514-555-0182<span class="sep">|</span>48 Lavigne Ouest, Suite 210<span class="sep">|</span>www.cdvalmorin-example.com</footer>
</main>
</body>
</html>
```